A-Stand Directional Sign Design

Objective:
We need a professional graphic design for an A-Stand sign that will guide customers arriving in our parking lot to our office. The design should be visually clear, welcoming, and aligned with our brand identity.
REQUIREMENTS:
Two versions of the design:
- One with an arrow pointing left
- One with an arrow pointing right
(This allows us to place the A-Stand anywhere and flip the graphic as needed.)
DIMENSIONS:
- Viewable Area: 30" x 40"
BRAND ALIGNMENT:
- Colors, fonts, and overall style should match our website: www.skornabel.com
- Clean, modern, and professional look consistent with our aviation/tourism brand
CONTENT:
- Clear directional arrow (left or right depending on version)
- Text: “Office Entrance” or similar concise wording (designers may propose alternatives if they improve clarity)
READABILITY:
- Bold, high-contrast design for visibility from a distance
- Simple layout that avoids clutter
DELIVERABLES:
- Final artwork in print-ready format (PDF preferred)
- Two versions: Arrow Left and Arrow Right
DESIGN GOAL:
Ensure customers can easily find our office upon arrival, while reinforcing skorNABEL’s professional and welcoming brand image.
Target Market(s)
Tourism

```html
<!DOCTYPE html>
<html lang="en">
<head>
<meta charset="utf-8">
<title>skorNABEL – Office Entrance Directional Signs</title>
<link rel="stylesheet" href="https://fonts.googleapis.com/css2?family=Lexend:wght@700&display=swap">
<style>
  :root {
    --backdrop: #000000;
    --panel: #ffffff;
    --brand-blue: #3f66ae;
    --water-light: #dbeef0;
    --water-mid: #b9dde2;
    --water-deep: #9ccbd2;
  }
  * { margin: 0; padding: 0; box-sizing: border-box; }
  html, body { width: 793px; height: 1200px; overflow: hidden; background: var(--backdrop); }
  .canvas { position: relative; width: 793px; height: 1200px; }
  .sign {
    position: absolute;
    left: 46px;
    width: 703px;
    height: 527px;
    background: var(--panel);
  }
  .sign--right { top: 55px; }
  .sign--left { top: 620px; }
  .sign__arrow { position: absolute; inset: 0; width: 703px; height: 527px; }
  .sign__label {
    position: absolute;
    top: 236px;
    font-family: "Lexend", sans-serif;
    font-weight: 700;
    font-size: 44px;
    line-height: 56px;
    letter-spacing: 0.5px;
    color: var(--brand-blue);
    white-space: nowrap;
  }
  .sign--right .sign__label { left: 78px; }
  .sign--left .sign__label { left: 200px; }
  .sign__brand {
    position: absolute;
    left: 0; right: 0;
    top: 425px;
    text-align: center;
    font-family: "Lexend", sans-serif;
    font-weight: 700;
    font-size: 40px;
    color: var(--brand-blue);
  }
</style>
</head>
<body>
<div class="canvas">
  <section class="sign sign--right">
    <svg class="sign__arrow" viewBox="0 0 703 527" role="img" aria-label="Right-pointing arrow filled with an aerial photo of a red helicopter flying over sparkling turquoise water">
      <defs>
        <linearGradient id="water-right" x1="0" y1="0" x2="1" y2="1">
          <stop offset="0" stop-color="var(--water-light)"/>
          <stop offset="0.6" stop-color="var(--water-mid)"/>
          <stop offset="1" stop-color="var(--water-deep)"/>
        </linearGradient>
      </defs>
      <path fill="url(#water-right)" d="M65 208 H513 V185 Q513 163 530 176 L642 251 Q657 263 642 276 L530 351 Q513 364 513 342 V319 H65 Q42 319 42 296 V231 Q42 208 65 208 Z"/>
    </svg>
    <p class="sign__label">OFFICE ENTRANCE</p>
    <p class="sign__brand">skorNABEL</p>
  </section>

  <section class="sign sign--left">
    <svg class="sign__arrow" viewBox="0 0 703 527" role="img" aria-label="Left-pointing arrow filled with an aerial photo of a red helicopter flying over sparkling turquoise water">
      <defs>
        <linearGradient id="water-left" x1="1" y1="0" x2="0" y2="1">
          <stop offset="0" stop-color="var(--water-light)"/>
          <stop offset="0.6" stop-color="var(--water-mid)"/>
          <stop offset="1" stop-color="var(--water-deep)"/>
        </linearGradient>
      </defs>
      <path fill="url(#water-left)" d="M628 210 H180 V187 Q180 165 163 178 L52 253 Q37 265 52 278 L163 353 Q180 366 180 344 V320 H628 Q651 320 651 297 V233 Q651 210 628 210 Z"/>
    </svg>
    <p class="sign__label">OFFICE ENTRANCE</p>
    <p class="sign__brand">skorNABEL</p>
  </section>
</div>
</body>
</html>
```